'Ormel Property Development' Business Card

Business Card Features:

High Quality (potentially textured) thick card - preference is white textured card

Logo (supplied)

We plan to use the vertical logo as the main logo. But i am happy for people to use either if they find it works better for the design of the card.

The building icon and also the insert to the 'E' is in a metallic finish, i think this should be finished in a metallic embossed or raised style.
Updates

Please note i have attached both a horizontal and Vertical Logo for your reference. We plan to use the vertical logo as the main logo. But i am happy for people to use either if they find it works better for the design of the card.

Please note i am considering having the cards made on stainless steel. This introduces the option of having cut outs in the card and etching or printing for the design. If you have a good concept for this please submit.

http://www.tinquarry.example/black-metal-cards# this is a site that makes the metal cards to offer some direction . . . . Please note i am basic the selection o the best design, if that means normal print cards on paper then this is what i will choose. But there are some great options with the metal. Thanks.

Industry/Entity Type

Building

Requirements
Must have
• Helvetica font to details side of card - logo as supplied to opposite side.

Card Details:

Darrow Pketts
Managing Director

+61 487 263 518
+61 3 6172 4809

PO Box 73
Bentleigh, VIC 3024

darrow@ormel.example

www.ormel.example

```html
<!DOCTYPE html>
<html lang="en">
<head>
<meta charset="utf-8">
<title>Ormel Property Development — Business Card</title>
<link rel="stylesheet" href="https://fonts.googleapis.com/css2?family=Arimo:wght@400;700&display=swap">
<style>
  :root {
    --page: #ecebea;
    --card-dark: #1b1b1c;
    --card-mid: #2a2a2b;
    --rose-gold: #e9b9a6;
    --rose-gold-deep: #c98d78;
    --text-light: #b9b9bb;
    --text-soft: #a4a4a7;
    --icon: #9d9da0;
  }
  * { box-sizing: border-box; margin: 0; padding: 0; }
  html, body {
    width: 1200px; height: 805px; overflow: hidden;
    background: var(--page);
    font-family: "Arimo", Helvetica, Arial, sans-serif;
  }
  .canvas { position: relative; width: 1200px; height: 805px; }

  .card {
    position: absolute; left: 170px; top: 170px;
    width: 860px; height: 465px; border-radius: 34px;
    background:
      repeating-linear-gradient(0deg, rgba(255,255,255,0.025) 0 1px, transparent 1px 3px),
      linear-gradient(135deg, var(--card-mid), var(--card-dark) 60%, #141415);
    box-shadow: 0 18px 40px rgba(0,0,0,0.25);
  }

  .brand {
    position: absolute; left: 70px; top: 110px; width: 260px;
    display: flex; flex-direction: column; align-items: flex-start; gap: 26px;
  }
  .brand-mark {
    width: 46px; height: 46px; background: var(--rose-gold);
  }
  .brand-name {
    color: var(--rose-gold);
    font-weight: 700; font-size: 30px; line-height: 1.25;
    letter-spacing: 1px;
  }

  .divider {
    position: absolute; left: 362px; top: 60px;
    width: 3px; height: 345px;
    background: linear-gradient(180deg, var(--rose-gold), var(--rose-gold-deep));
  }

  .details { position: absolute; left: 412px; top: 100px; right: 40px; }
  .person-name { color: var(--text-light); font-size: 36px; font-weight: 400; }
  .person-role { color: var(--text-soft); font-size: 17px; margin-top: 18px; }

  .contacts { list-style: none; margin-top: 80px; }
  .contacts li {
    display: flex; align-items: center; gap: 10px;
    color: var(--text-light); font-size: 18px; margin-bottom: 13px;
  }
  .contacts .pair { gap: 26px; }
  .contacts .item { display: flex; align-items: center; gap: 10px; }
  .icon { width: 18px; height: 18px; fill: var(--icon); flex: none; }
</style>
</head>
<body>
<main class="canvas">
  <section class="card">
    <div class="brand">
      <div class="brand-mark"></div>
      <p class="brand-name">ORMEL<br>Property Development</p>
    </div>

    <div class="divider"></div>

    <div class="details">
      <h1 class="person-name">Darrow Pketts</h1>
      <p class="person-role">Managing Director</p>

      <ul class="contacts">
        <li class="pair">
          <span class="item">
            <svg class="icon" viewBox="0 0 18 18"><path d="M5 1h8a1 1 0 0 1 1 1v14a1 1 0 0 1-1 1H5a1 1 0 0 1-1-1V2a1 1 0 0 1 1-1zm1 2v10h6V3zm3 11a1 1 0 1 0 0 2 1 1 0 0 0 0-2z"/></svg>
            0487263518
          </span>
          <span class="item">
            <svg class="icon" viewBox="0 0 18 18"><rect x="0" y="0" width="18" height="18" rx="3"/><path fill="#1f1f20" d="M5 3.5l2 2-1 1.5a7 7 0 0 0 4 4l1.5-1 2 2-1.2 2C8.5 14 4 9.5 3.9 5z"/></svg>
            1800 614 207
          </span>
        </li>
        <li>
          <svg class="icon" viewBox="0 0 18 18"><rect width="18" height="18" rx="3"/><path fill="#1f1f20" d="M9 3a4 4 0 0 0-4 4c0 3 4 8 4 8s4-5 4-8a4 4 0 0 0-4-4zm0 5.5A1.5 1.5 0 1 1 9 5.5a1.5 1.5 0 0 1 0 3z"/></svg>
          PO BOX 73 Bentleigh, VIC 3024
        </li>
        <li>
          <svg class="icon" viewBox="0 0 18 18"><rect x="1" y="3" width="16" height="12" rx="2"/><rect fill="#1f1f20" x="3" y="5" width="12" height="6"/></svg>
          darrow@ormel.example
        </li>
        <li>
          <svg class="icon" viewBox="0 0 18 18"><path d="M9 1a8 8 0 1 0 0 16A8 8 0 0 0 9 1zm5.9 7h-3a12 12 0 0 0-1-4.8A6 6 0 0 1 14.9 8zM9 3.1c.8 1.1 1.4 2.9 1.5 4.9h-3c.1-2 .7-3.8 1.5-4.9zM7.1 3.2A12 12 0 0 0 6.1 8h-3a6 6 0 0 1 4-4.8zM3.1 10h3a12 12 0 0 0 1 4.8 6 6 0 0 1-4-4.8zM9 14.9c-.8-1.1-1.4-2.9-1.5-4.9h3c-.1 2-.7 3.8-1.5 4.9zm1.9-.1a12 12 0 0 0 1-4.8h3a6 6 0 0 1-4 4.8z"/></svg>
          www.ormel.example
        </li>
      </ul>
    </div>
  </section>
</main>
</body>
</html>
```